Photography Business, Business Card

Looking for a unique cutting edge card that takes advantage of the latest printing technologies. Please review this site for all the options they office: https://plumeprints.example. If you can think it they can do it. And if you have an idea and do not know if they can do it, I will check into it.
Updates

Target Market(s)

People and places I took images of and future clients.

Industry/Entity Type

Photography

Contact Information for Business Card

Name, cell & email. Colin Hartley, chartley@kvnphoto.example, 318-742-9061

Colors

Designer to choose only greyscale colors for use in the design.

Requirements
Must have
• 100% cutting edge. Is so great, those I hand it to always show it to someone else. A piece of art.
Nice to have
• Blacks, silvers, greys, some red. Maybe other colors?

```html
<!DOCTYPE html>
<html lang="en">
<head>
<meta charset="UTF-8">
<title>KVN Multimedia – Business Card</title>
<link rel="stylesheet" href="https://fonts.googleapis.com/css2?family=Arimo:wght@400;700&family=Lato:wght@700&display=swap">
<style>
  :root {
    --canvas: #ffffff;
    --card-light: #e9eaeb;
    --card-dark: #232323;
    --ink: #222222;
    --ink-soft: #555555;
    --ink-muted: #7a7a7a;
    --accent: #22b04b;
    --paper: #ffffff;
  }
  * { margin: 0; padding: 0; box-sizing: border-box; }
  html, body {
    width: 1200px;
    height: 1200px;
    overflow: hidden;
    background: var(--canvas);
  }
  .canvas {
    position: relative;
    width: 1200px;
    height: 1200px;
  }
  .card {
    position: absolute;
    left: 200px;
    width: 798px;
    height: 456px;
    border-radius: 38px;
  }
  .card--front { top: 97px; background: var(--card-light); }
  .card--back  { top: 604px; background: var(--card-dark); }

  /* Front */
  .brand-tag {
    position: absolute;
    top: 132px;
    right: 60px;
    display: flex;
    align-items: center;
    gap: 14px;
  }
  .brand-tag__dot {
    width: 34px;
    height: 34px;
    border-radius: 50%;
    background: var(--accent);
  }
  .brand-tag__name {
    font-family: "Lato", sans-serif;
    font-weight: 700;
    font-size: 28px;
    color: var(--ink);
  }
  .person {
    position: absolute;
    left: 105px;
    top: 196px;
  }
  .person__name {
    font-family: "Arimo", sans-serif;
    font-size: 43px;
    font-weight: 400;
    color: var(--ink);
    line-height: 1;
    letter-spacing: -0.3px;
  }
  .person__name strong { font-weight: 700; }
  .person__role {
    margin-top: 14px;
    font-family: "Arimo", sans-serif;
    font-size: 25px;
    color: var(--ink-muted);
    letter-spacing: 0.3px;
  }
  .contact {
    position: absolute;
    left: 96px;
    top: 322px;
    list-style: none;
    font-family: "Arimo", sans-serif;
    color: var(--ink-soft);
  }
  .contact__item {
    display: flex;
    align-items: center;
    gap: 12px;
  }
  .contact__item--phone { font-size: 26px; }
  .contact__item--email { font-size: 23px; margin-top: 16px; }
  .contact__icon {
    width: 30px;
    height: 30px;
    flex: none;
    fill: none;
    stroke: var(--ink-soft);
    stroke-width: 1.6;
    stroke-linejoin: round;
  }

  /* Back */
  .brand-lockup {
    position: absolute;
    inset: 0;
    display: flex;
    align-items: center;
    justify-content: center;
    gap: 18px;
  }
  .brand-lockup__dot {
    width: 44px;
    height: 44px;
    border-radius: 50%;
    background: var(--accent);
  }
  .brand-lockup__name {
    font-family: "Lato", sans-serif;
    font-weight: 700;
    font-size: 42px;
    color: var(--paper);
    letter-spacing: 0.5px;
  }
</style>
</head>
<body>
<main class="canvas">
  <section class="card card--front" aria-label="Card front">
    <div class="brand-tag">
      <span class="brand-tag__dot"></span>
      <span class="brand-tag__name">KVN Multimedia</span>
    </div>
    <div class="person">
      <h1 class="person__name"><strong>Colin</strong> Hartley</h1>
      <p class="person__role">Creative Visual Services</p>
    </div>
    <ul class="contact">
      <li class="contact__item contact__item--phone">
        <svg class="contact__icon" viewBox="0 0 24 24" aria-hidden="true">
          <path d="M5 3h4l2 5-2.5 1.5a11 11 0 0 0 6 6L16 13l5 2v4a2 2 0 0 1-2 2A17 17 0 0 1 3 5a2 2 0 0 1 2-2z"/>
        </svg>
        <span>(318)742-9061</span>
      </li>
      <li class="contact__item contact__item--email">
        <svg class="contact__icon" viewBox="0 0 24 24" aria-hidden="true">
          <rect x="2" y="5" width="20" height="14"/>
          <path d="M2 5l10 8 10-8M2 19l7-7M22 19l-7-7"/>
        </svg>
        <span>chartley@kvnphoto.example</span>
      </li>
    </ul>
  </section>

  <section class="card card--back" aria-label="Card back">
    <div class="brand-lockup">
      <span class="brand-lockup__dot"></span>
      <span class="brand-lockup__name">KVN Multimedia</span>
    </div>
  </section>
</main>
</body>
</html>
```